spot uv business card design for QRT Mechanics

I need a great new business card design best suited for spot uv printing. Details to include are Desmond Hollis 0491227305 wwwqrtmech.com.au, des@qrtmech.com.au. Company logo attached.
The design has to be spot uv/varnish optimised!!
Business

```html
<!DOCTYPE html>
<html lang="en">
<head>
<meta charset="utf-8">
<title>QRT Mechanics – Business Card</title>
<link rel="stylesheet" href="https://fonts.googleapis.com/css2?family=Open+Sans:wght@300;400&display=swap">
<style>
  :root {
    --sheet: #ffffff;
    --frame: #9a9a9a;
    --card-edge: #222222;
    --teal: #123d4a;
    --teal-soft: #16485a;
    --on-teal: #ffffff;
  }
  html, body {
    margin: 0;
    padding: 0;
    width: 1200px;
    height: 364px;
    overflow: hidden;
    background: var(--sheet);
    font-family: "Open Sans", Arial, sans-serif;
  }
  .sheet {
    position: relative;
    width: 1198px;
    height: 362px;
    border: 1px solid var(--frame);
    background: var(--sheet);
  }
  .card {
    position: absolute;
    top: 29px;
    width: 540px;
    height: 281px;
    box-sizing: border-box;
  }
  .card--front {
    left: 58px;
    background: var(--sheet);
    border: 1.5px solid var(--card-edge);
    border-radius: 0 44px 0 44px;
  }
  .card--back {
    left: 640px;
    width: 536px;
    color: var(--on-teal);
    border-radius: 44px 0 44px 0;
    overflow: hidden;
  }
  .back-texture {
    position: absolute;
    inset: 0;
    background: linear-gradient(135deg, var(--teal-soft), var(--teal));
  }
  .wordmark {
    position: absolute;
    left: 84px;
    top: 116px;
    display: flex;
    align-items: center;
    gap: 14px;
    color: var(--teal);
  }
  .wordmark__square {
    width: 44px;
    height: 44px;
    background: var(--teal);
    border-radius: 4px;
  }
  .wordmark__name {
    font-size: 38px;
    font-weight: 300;
    letter-spacing: 0.5px;
    text-transform: uppercase;
    line-height: 1;
  }
  .holder {
    position: absolute;
    left: 38px;
    top: 110px;
    margin: 0;
    font-size: 22px;
    font-weight: 400;
  }
  .contacts {
    position: absolute;
    left: 44px;
    top: 180px;
    margin: 0;
    padding: 0;
    list-style: none;
    font-size: 16px;
    font-weight: 400;
  }
  .contacts li {
    display: flex;
    align-items: center;
    gap: 9px;
    height: 24px;
  }
  .contacts li.contacts__phone { margin-bottom: 10px; }
  .contacts svg { width: 14px; height: 14px; fill: var(--on-teal); flex: none; }
</style>
</head>
<body>
<div class="sheet">
  <section class="card card--front" aria-label="Card front">
    <div class="wordmark">
      <span class="wordmark__square"></span>
      <span class="wordmark__name">QRT Mechanics</span>
    </div>
  </section>

  <section class="card card--back" aria-label="Card back">
    <div class="back-texture" role="img" aria-label="Spot UV texture of repeated company name tiles"></div>
    <h1 class="holder">Desmond Hollis</h1>
    <ul class="contacts">
      <li class="contacts__phone">
        <svg viewBox="0 0 24 24" aria-hidden="true"><path d="M6.6 10.8a15.1 15.1 0 0 0 6.6 6.6l2.2-2.2a1 1 0 0 1 1-.25 11.4 11.4 0 0 0 3.6.57 1 1 0 0 1 1 1V20a1 1 0 0 1-1 1A17 17 0 0 1 3 4a1 1 0 0 1 1-1h3.5a1 1 0 0 1 1 1c0 1.25.2 2.45.57 3.57a1 1 0 0 1-.25 1z"/></svg>
        <span>0491 227 305</span>
      </li>
      <li>
        <svg viewBox="0 0 24 24" aria-hidden="true"><path d="M2 6h20v12H2z M2 6l10 7 10-7" fill="none" stroke="#fff" stroke-width="2.4"/></svg>
        <span>des@qrtmech.com.au</span>
      </li>
      <li>
        <svg viewBox="0 0 24 24" aria-hidden="true"><circle cx="12" cy="12" r="9.5" fill="none" stroke="#fff" stroke-width="2.2"/><path d="M2.5 12h19M12 2.5c3 3 3 16 0 19M12 2.5c-3 3-3 16 0 19" fill="none" stroke="#fff" stroke-width="1.8"/></svg>
        <span>wwwqrtmech.com.au</span>
      </li>
    </ul>
  </section>
</div>
</body>
</html>
```